Sightless Fellowship Hall of San Diego needs an ad/flyer for convention program

Established in 1949, the Sightless Fellowship Hall of San Diego's mission is to enrich the lives of blind and visually impaired adults by preparing them for a normal, active life in a society that is principally sighted by encouraging independence.

Located in Harwick Gardens in San Diego, California, we are a nonprofit that gives blind and visually impaired people in our community an opportunity to socialize and interact. We help members build skills, confidence, and self-esteem through our various social, recreational, and educational activities. We were founded partially by Heron Guild members and receive ongoing funding from them.

We need an 8 1/2 by 11 inch color ad in jpg format. We would like it to be editable. This will be the foundation of our rebranding. The ad will be in a meeting program of the California Herons (californiaherons.example) with the goal of highlighting some of our programs in order to solicit donations from individual Heron Guilds, preferably ongoing ones.

We would like the ad to be generic enough that we can use the ad for other events and as a flyer in the future. We want the ad/flyer to be classic but eye popping with color. We want the design to reflect a professional and lively organization that loves to serve our members. We don’t entirely love our logo, but it’s what we have for now. Our next task will be a new logo design.

We would like to highlight some of our programs for our members include bingo, blind waterskiing and surfing, cooking and ceramic classes, foreign language classes, self defense classes, yoga, and craft classes. Many of the crafts our members make are sold during fundraisers, and they include blankets, scarves, beaded animals, and more. See a sampling of pictures. We provide transportation to and from our Center, free lunch while at the Center, and food to take home. Many of these activities continue during the pandemic via online platforms. We are doing monthly home deliveries of food to our members.

We need donations to keep our programs going, and we have building repairs & maintenance that we need donations in order to complete. See attached document regarding donations. Please reach out if you have questions. Thank you.

Web address: sfhsd.example
Street address: The Sightless Fellowship Hall of San Diego, 2716 Merrow St San Diego, CA 92107
Email address: donation@sfhsd.example
To make a donation: https://sfhsd.example/donate-2/

Donors

NonProfit

Sans Serif

Must have
• Highlight programs and information on how to make a donation.
Nice to have
• Information on how much each dollar donated will go - see attachment
Should not have
• Unprofessional or sloppy details

```html
<!DOCTYPE html>
<html lang="en">
<head>
<meta charset="utf-8">
<title>Sightless Fellowship Hall of San Diego – Convention Program Flyer</title>
<link href="https://fonts.googleapis.com/css2?family=Bebas+Neue&family=Montserrat:wght@400;500;600;700;800&display=swap" rel="stylesheet">
<style>
:root{
  --page:#eceef1;
  --ink:#111318;
  --navy:#151b2e;
  --blue:#1d4f9c;
  --blue-bright:#1f5bb5;
  --panel-light:#dbe3ee;
  --gold:#8c7b46;
  --white:#ffffff;
  --badge:#e8b820;
}
*{margin:0;padding:0;box-sizing:border-box}
html,body{width:691px;height:1200px;overflow:hidden;background:var(--page)}
body{font-family:"Montserrat",sans-serif;color:var(--ink);position:relative}
.flyer{position:absolute;left:0;top:153px;width:691px;height:894px;overflow:hidden;background:var(--panel-light)}
.abs{position:absolute}

/* left side */
.left-bg{left:0;top:0;width:400px;height:894px;background:linear-gradient(180deg,#e9eef5 0%,#d5dfec 60%,#cfd9e8 100%)}
.swoosh{left:0;top:0;width:400px;height:460px}
.wordmark{left:42px;top:58px;font-family:"Montserrat",sans-serif;font-weight:800;font-size:40px;letter-spacing:2px;color:var(--ink)}
.wordmark-box{left:42px;top:40px;width:14px;height:14px;background:var(--ink)}
.photo{border-radius:50%;border:3px solid var(--white);box-shadow:0 2px 5px rgba(0,0,0,.35)}
.photo-kids{left:227px;top:18px;width:160px;height:160px;background:radial-gradient(circle at 40% 45%,#d9c2ad,#7c9bb8 60%,#36506f)}
.photo-beads{left:154px;top:365px;width:68px;height:68px;background:radial-gradient(circle at 50% 55%,#2b3f9c,#8ea0c8 60%,#d7dbe3)}
.photo-blankets{left:230px;top:343px;width:106px;height:106px;background:linear-gradient(160deg,#d58fb0,#8fc5d6 50%,#e7d8e6)}
.photo-penguin{left:296px;top:297px;width:102px;height:102px;background:radial-gradient(circle at 50% 50%,#2b2b30,#9a9ea6 55%,#e2e4e8)}

.title{left:31px;font-family:"Bebas Neue",sans-serif;color:var(--ink);line-height:1;white-space:nowrap}
.t1{top:131px;font-size:47px}
.t2{top:178px;font-size:44px}
.t3{top:229px;font-size:38px}
.t4{left:31px;font-weight:800;color:var(--blue);line-height:1;font-size:37px;letter-spacing:-.5px;white-space:nowrap}
.t4a{top:272px}.t4b{top:312px}

.did-you-know{left:31px;top:447px;font-weight:700;font-size:25px}
.fact{left:31px;width:332px;display:flex;gap:11px;font-size:8.3px;line-height:10.6px;color:#222}
.fact-icon{flex:0 0 27px;height:27px;border-radius:50%;background:var(--navy);border:3px solid #9aa3b0;display:flex;align-items:center;justify-content:center}
.fact-icon svg{width:13px;height:13px}
.fact b{font-weight:700}
.f1{top:495px}.f2{top:537px}.f3{top:601px}.f4{top:632px}.f5{top:663px}

.sponsor{left:45px;top:724px;width:273px;height:42px;background:var(--white);border:1.5px solid var(--navy);display:flex;align-items:center;justify-content:space-around}
.sponsor-price{font-family:"Bebas Neue",sans-serif;font-size:25px;color:var(--blue);line-height:.9;white-space:nowrap}
.sponsor-label{font-size:9px;font-weight:700;line-height:1}
.sponsor-divider{width:1px;height:30px;background:#9aa3b0}
.contact-btn{left:45px;top:793px;width:115px;height:25px;border-radius:13px;background:var(--blue-bright);color:var(--white);font-weight:600;font-size:12.5px;display:flex;align-items:center;justify-content:center}

.footer{left:0;top:816px;width:420px;height:78px;background:var(--navy)}
.foot-item{display:flex;gap:7px;color:var(--white);font-size:9.2px;font-weight:600;line-height:10.6px}
.foot-item svg{flex:0 0 12px;width:12px;height:12px;margin-top:1px}
.fi-address{left:32px;top:834px;width:180px}
.fi-email{left:229px;top:834px;white-space:nowrap}
.fi-web{left:229px;top:856px;white-space:nowrap}

/* right panel */
.right{left:395px;top:0;width:296px;height:700px;background:linear-gradient(180deg,#000 0%,#0c0c0f 60%,#141418 100%)}
.pre-covid{left:409px;top:28px;font-weight:800;font-size:29px;color:var(--white)}
.tier{left:395px;width:296px;height:26px;background:var(--blue);color:var(--white);font-weight:700;font-size:13.5px;padding-left:12px;display:flex;align-items:center;white-space:nowrap}
.tier sup{font-size:7px;margin-right:1px}
.tr1{top:68px}.tr2{top:192px}.tr3{top:303px}.tr4{top:396px}
.buy{left:413px;width:265px;display:flex;gap:7px;color:var(--white);line-height:1.25}
.buy::before{content:"";flex:0 0 5px;height:5px;margin-top:3px;border-radius:50%;background:var(--white)}
.buy.small{font-size:7.6px}
.buy.large{font-size:9.6px}
.b1{top:110px}.b2{top:141px}.b3{top:158px}
.b4{top:236px}.b5{top:269px}
.b6{top:342px}.b7{top:361px}
.b8{top:432px}

.fund-box{left:409px;top:480px;width:251px;height:87px;border:1.5px solid #cfd3da}
.fund-amount{font-weight:800;font-size:21px;color:var(--white);line-height:1}
.fund-sub{font-size:9.5px;font-weight:500;color:var(--white)}
.fa1{left:423px;top:490px}.fs1{left:423px;top:513px}
.fa2{left:563px;top:490px}.fs2{left:563px;top:513px}
.fund-divider{left:531px;top:492px;width:2px;height:30px;background:var(--white)}
.fund-band{left:425px;top:531px;width:224px;height:32px;background:var(--white);color:var(--ink);font-size:10px;font-weight:600;text-align:center;line-height:13px;padding-top:3px}
.fund-band b{font-weight:800}

.every{left:395px;width:296px;text-align:center;color:var(--white);line-height:1}
.e1{top:588px;font-size:14.5px;font-weight:600;letter-spacing:.3px}
.e2{top:603px;font-size:13px;font-weight:500;letter-spacing:.4px}
.e3{left:432px;top:618px;width:219px;height:16px;border:1px solid #cfd3da;color:var(--white);font-size:10px;text-align:center;line-height:14px;letter-spacing:.3px;white-space:nowrap}

.donate-art{left:300px;top:630px;width:391px;height:264px}
.donate-head{left:395px;top:723px;width:296px;text-align:center;font-weight:700;font-size:13px;color:var(--ink)}
.donate-url{left:416px;top:741px;width:250px;height:20px;border-radius:10px;background:var(--blue-bright);color:var(--white);font-weight:700;font-size:10px;white-space:nowrap;display:flex;align-items:center;justify-content:center;letter-spacing:.1px}
.partner-name{left:421px;top:790px;font-weight:600;font-size:15px;line-height:15px;color:var(--ink)}
.partner-rule{left:421px;top:829px;width:150px;height:1px;background:#333}
.partner-web{left:421px;top:843px;display:flex;gap:6px;align-items:center;font-weight:700;font-size:10px;color:var(--ink);white-space:nowrap}
.partner-web svg{width:14px;height:14px}
.partner-badge{left:593px;top:807px;width:70px;height:70px;border-radius:50%;background:var(--badge);border:3px solid var(--blue)}
</style>
</head>
<body>
<main class="flyer">

  <div class="abs left-bg"></div>
  <svg class="abs swoosh" viewBox="0 0 400 460" aria-hidden="true">
    <path d="M0 0 H182 C320 90 390 240 350 335 C315 400 150 400 0 352 Z" fill="#ffffff"/>
    <path d="M182 0 C320 90 392 240 352 336" fill="none" stroke="var(--gold)" stroke-width="7"/>
    <path d="M196 0 C336 96 402 250 360 342" fill="none" stroke="#1c1c22" stroke-width="4"/>
    <path d="M0 352 C120 392 260 400 340 352" fill="none" stroke="#1c1c22" stroke-width="5"/>
    <path d="M0 362 C130 404 270 410 346 360" fill="none" stroke="var(--gold)" stroke-width="3"/>
  </svg>

  <div class="abs wordmark-box"></div>
  <div class="abs wordmark">SFH</div>

  <div class="abs photo photo-kids" role="img" aria-label="Photo of a woman helping a young boy with a tablet"></div>

  <div class="abs title t1">SIGHTLESS</div>
  <div class="abs title t2">FELLOWSHIP HALL</div>
  <div class="abs title t3">OF SAN DIEGO</div>
  <div class="abs t4 t4a">CONVENTION</div>
  <div class="abs t4 t4b">PROGRAM</div>

  <div class="abs photo photo-beads" role="img" aria-label="Photo of a blue beaded angel craft"></div>
  <div class="abs photo photo-blankets" role="img" aria-label="Photo of stacked handmade knitted blankets"></div>
  <div class="abs photo photo-penguin" role="img" aria-label="Photo of a handmade beaded penguin"></div>

  <h2 class="abs did-you-know">Did you know?</h2>

  <div class="abs fact f1">
    <span class="fact-icon"><svg viewBox="0 0 16 16"><circle cx="8" cy="8" r="5" fill="none" stroke="#fff" stroke-width="1.6"/></svg></span>
    <p>During the pandemic we offer Bingo, Trivia and other virtual games every week, where blind and low vision participants can win SFH bucks.&nbsp; You can sponsor one day of games for $35.</p>
  </div>
  <div class="abs fact f2">
    <span class="fact-icon"><svg viewBox="0 0 16 16"><path d="M3 8 L8 3 L13 8 V13 H3 Z" fill="none" stroke="#fff" stroke-width="1.6"/></svg></span>
    <p>You can provide 75 gift bags for our ‘We are in This Together’ home delivery program.&nbsp; Many of our blind and low vision people are isolated and stuck at home.&nbsp; These gift packages are welcomed with enthusiasm and gratefulness.&nbsp; Your rewards are huge smiles and happy faces.</p>
  </div>
  <div class="abs fact f3">
    <span class="fact-icon"><svg viewBox="0 0 16 16"><rect x="3" y="4" width="10" height="9" fill="none" stroke="#fff" stroke-width="1.6"/></svg></span>
    <p>Our building is over 20 years old and requires ongoing maintenance and repairs</p>
  </div>
  <div class="abs fact f4">
    <span class="fact-icon"><svg viewBox="0 0 16 16"><path d="M3 3 H13 V13 H3 Z M6 3 V13 M10 3 V13" fill="none" stroke="#fff" stroke-width="1.4"/></svg></span>
    <p>Fencing (cage) required to protect outside air conditioning units from vandalism.&nbsp; Cost: $2,500</p>
  </div>
  <div class="abs fact f5">
    <span class="fact-icon"><svg viewBox="0 0 16 16"><path d="M3 8 L7 12 L13 4" fill="none" stroke="#fff" stroke-width="1.8"/></svg></span>
    <p>Wanted: <b>Sponsors FOR WEEKLY VIRTUAL BINGO AND TRIVIA GAMES:</b> Blind and Low vision participants receive one SFH buck per win. SFH bucks are turned into gift cards &amp; CTL transportation passes.</p>
  </div>

  <div class="abs sponsor">
    <div class="sponsor-item"><div class="sponsor-price">1 WEEK $40</div><div class="sponsor-label">SPONSOR FOR</div></div>
    <span class="sponsor-divider"></span>
    <div class="sponsor-item"><div class="sponsor-price">1 MONTH $160</div><div class="sponsor-label">SPONSOR FOR</div></div>
  </div>

  <div class="abs contact-btn">Contact Now</div>

  <div class="abs footer"></div>
  <div class="abs foot-item fi-address">
    <svg viewBox="0 0 12 12"><path d="M6 11 C3 7 2 5.5 2 4 A4 4 0 0 1 10 4 C10 5.5 9 7 6 11 Z" fill="#fff"/><circle cx="6" cy="4" r="1.5" fill="var(--navy)"/></svg>
    <span>The Sightless Fellowship Hall of San Diego,<br>2716 Merrow St San Diego,<br>CA 92107</span>
  </div>
  <div class="abs foot-item fi-email">
    <svg viewBox="0 0 12 12"><rect x="1" y="2.5" width="10" height="7" fill="#fff"/><path d="M1 2.5 L6 6.5 L11 2.5" fill="none" stroke="var(--navy)" stroke-width="1"/></svg>
    <span>donation@sfhsd.example</span>
  </div>
  <div class="abs foot-item fi-web">
    <svg viewBox="0 0 12 12"><circle cx="6" cy="6" r="5" fill="none" stroke="#fff" stroke-width="1.2"/><path d="M1 6 H11 M6 1 C3.5 4 3.5 8 6 11 M6 1 C8.5 4 8.5 8 6 11" fill="none" stroke="#fff" stroke-width="1"/></svg>
    <span>www.sfhsd.example</span>
  </div>

  <div class="abs right"></div>
  <h2 class="abs pre-covid">Pre-Covid:</h2>

  <div class="abs tier tr1"><sup>$</sup>10 per month or&nbsp;<sup>$</sup>120 will buy:</div>
  <p class="abs buy small b1">60 meals for our lunch program – we serve 130<br>meals each week</p>
  <p class="abs buy small b2">13 round trip CTL transportation tickets</p>
  <p class="abs buy small b3">Enough beads to make 35 Dora Vale angels in our<br>craft class</p>

  <div class="abs tier tr2"><sup>$</sup>20 per month or&nbsp;<sup>$</sup>240 will buy</div>
  <p class="abs buy large b4">26 round trip CTL transportation<br>tickets</p>
  <p class="abs buy large b5">One month of large print and Braille<br>translation newsletter printing</p>

  <div class="abs tier tr3"><sup>$</sup>50 per month or&nbsp;<sup>$</sup>600 will buy:</div>
  <p class="abs buy large b6">300 lunches</p>
  <p class="abs buy large b7">Thanksgiving dinner with all the<br>fixings for 80 to 100 guests</p>

  <div class="abs tier tr4"><sup>$</sup>100 per month or&nbsp;<sup>$</sup>1200 will buy:</div>
  <p class="abs buy large b8">Approximately 10 Bingo parties<br>including food and prizes</p>

  <div class="abs fund-box"></div>
  <div class="abs fund-amount fa1">$1,083</div>
  <div class="abs fund-sub fs1">PER MONTH</div>
  <div class="abs fund-divider"></div>
  <div class="abs fund-amount fa2">$13,000</div>
  <div class="abs fund-sub fs2">PER YEAR</div>
  <div class="abs fund-band">will fund our entire <b>lunch program</b><br>for the year.</div>

  <div class="abs every e1">EVERY DOLLAR DONATED</div>
  <div class="abs every e2">GOES TO SUPPORT</div>
  <div class="abs e3">SFH PARTICIPANTS &amp; PROGRAMS</div>

  <svg class="abs donate-art" viewBox="0 0 391 264" role="img" aria-label="Black and white photo of smiling volunteers and members">
    <defs>
      <linearGradient id="photoTone" x1="0" y1="0" x2="1" y2="0">
        <stop offset="0" stop-color="#5d6066"/>
        <stop offset=".45" stop-color="#c9cbcf"/>
        <stop offset="1" stop-color="#7f8287"/>
      </linearGradient>
    </defs>
    <path d="M70 264 C58 150 110 70 220 52 C290 40 350 38 391 30 V264 Z" fill="url(#photoTone)"/>
    <path d="M70 264 C58 150 110 70 220 52 C290 40 350 38 391 30" fill="none" stroke="#1c1c22" stroke-width="6"/>
    <path d="M82 264 C72 158 120 82 224 64 C292 52 350 50 391 42" fill="none" stroke="#f2f3f5" stroke-width="3"/>
  </svg>

  <div class="abs donate-head">TO MAKE A DONATION:</div>
  <div class="abs donate-url">HTTPS://SFHSD.EXAMPLE/DONATE-2/</div>
  <div class="abs partner-name">California Heron<br>Guilds</div>
  <div class="abs partner-rule"></div>
  <div class="abs partner-web">
    <svg viewBox="0 0 14 14"><circle cx="7" cy="7" r="6" fill="none" stroke="#111" stroke-width="1.3"/><path d="M1 7 H13 M7 1 C4 4.5 4 9.5 7 13 M7 1 C10 4.5 10 9.5 7 13" fill="none" stroke="#111" stroke-width="1"/></svg>
    <span>californiaherons.example</span>
  </div>
  <div class="abs partner-badge"></div>

</main>
</body>
</html>
```